Law Firm Magazine Advertisement

The Company:
Thornbury Legal Partners is the largest management side women-owned employment law firm in the United States. For over a decade, we have devoted our practice exclusively to representing business in all aspects of California employment law and related litigation. Our firm represents startups to Paragon 300s from a wide range of industries including retail, restaurants, telecommunications, manufacturing, health care, finance, oil and high tech. Please see our website for more about us. www.thornburylegalpartners.example

The Ad:
We are looking for a new design for our advertisements in a major legal magazine. The magazine itself has a modern, graphical approach much like Vexel but for the legal/ business community.

Most advertisements are full page, and there is one every few pages. Some of these ads are text heavy, and others are full page photos. It is important that our ad stand out, as many of these other ads are for companies similar to us. We are looking to attract the attention of internal corporate counsel to the benefits of our outside assistance in their employment matters. We would like to maintain a professional but forward-thinking image.

We would like concepts for a full page magazine ad in black and white. We would like the designs to be based in artistic representations of our office (see photos for reference) and graphical in approach. Please do not use photos. We are looking for bold, eye-catching contrast and simple designs.

If you have any further questions, or would like clarification, please email Marisol at rdv@thornburylegalpartners.example
Updates

From looking at all of the designs that have been sent in so far, I would like to note that while we would like for the ad to fit in with our website design, we do not want it to look exactly the same. The paneled image approach is not necessarily what we are looking for. 

It is also important that the font in our logo remain the same. 

Thank you for your efforts so far.

I am in the process of obtaining more photos of our firm to post for you to use. There should be at least a few new ones by end of today or tomorrow (PST).

I have also been informed that we are removing the word "practical" from our marketing materials. Therefore, if you choose to use our words, please do not use the word "practical" in any future drafts. [I have changed this in the original brief as well, and will not penalize any designs strictly for using it, as it is easily changed later].

Our keywords are: proven, strategic, collaborative, cost effective, trial ready

We will also be adding a few additional logos to our ad for various awards and associations we are affiliated with. I will update the brief with these as soon as I have them. 

As another creative suggestion, do not shy away from adding more information about our firm. The first paragraph of the brief contains our marketing language, so feel free to integrate it into your design. 

Again, thank you for all of your efforts so far.

Thank you!

Upon review of all of the designs submitted, we did not find anything like what we were looking for, and therefore I have changed the brief, and some of the requirements. Please read it again and redesign. I apologize to any designers that may have designs in the works based on the old brief and ask that you try your hand at the new request. Below is the changed wording in the brief, but please read the "must have" and "nice to have" sections again. 

Thank you.

We would like the designs to be based in artistic representations of our office (see photos for reference) and graphical in approach. Please do not use photos. We are looking for bold, eye-catching contrast and simple designs.

Industry/Entity Type

Law Firm

Requirements
Must have
• Must be black and white.

Please include:
our logo OR Thornbury Legal Partners in Futura font.
California Employment Law for Business (our tagline)
San Francisco Los Angeles (our locations, no address please)
www.thornburylegalpartners.example (our website)
FQTOR Logo
GPDR BIK Logo
Top-tier Legal Shop Logo
Nice to have
• Artistic representation of our office

```html
<!DOCTYPE html>
<html lang="en">
<head>
<meta charset="utf-8">
<title>Thornbury Legal Partners — Advertisement</title>
<link href="https://fonts.googleapis.com/css2?family=Arimo:wght@400;700&family=Jost:wght@400&display=swap" rel="stylesheet">
<style>
  :root {
    --ink: #231f20;
    --ghost: #d2d2d2;
    --rule: #9d9d9d;
    --logo: #8a8a8a;
    --paper: #ffffff;
  }
  html, body { margin: 0; padding: 0; overflow: hidden; background: var(--paper); }
  .ad {
    position: relative;
    width: 928px;
    height: 1200px;
    overflow: hidden;
    background: var(--paper);
    font-family: "Arimo", Arial, sans-serif;
    font-weight: 700;
  }
  .band { position: absolute; left: 0; width: 928px; background: var(--rule); }
  .band--top { top: 0; height: 8px; }
  .band--bottom { bottom: 0; height: 12px; }

  .word-row {
    position: absolute;
    left: 53px;
    width: 820px;
    display: flex;
    justify-content: space-between;
    align-items: baseline;
    white-space: nowrap;
    line-height: 1;
  }
  .word-row--right { justify-content: flex-end; gap: 12px; }
  .ghost { color: var(--ghost); font-size: 43px; }
  .ghost--wide { letter-spacing: 0.22em; }
  .ghost--mid { letter-spacing: 0.08em; }
  .key { color: var(--ink); font-size: 84px; letter-spacing: -0.01em; }
  .key--wide { letter-spacing: 0.06em; }

  .firm-name {
    position: absolute;
    left: 53px;
    top: 1038px;
    font-family: "Jost", "Futura", sans-serif;
    font-weight: 400;
    color: var(--logo);
    line-height: 1;
  }
  .firm-name__main { display: block; font-size: 62px; letter-spacing: 0.01em; }
  .firm-name__sub { display: block; font-size: 16px; letter-spacing: 0.42em; margin-top: 12px; text-transform: uppercase; }

  .cert-badge {
    position: absolute;
    left: 404px;
    top: 1088px;
  }

  .contact {
    position: absolute;
    right: 55px;
    top: 1026px;
    text-align: right;
    font-weight: 400;
    font-size: 16px;
    line-height: 30.5px;
    color: var(--ink);
  }

  .footer-line {
    position: absolute;
    left: 53px;
    width: 822px;
    top: 1158px;
    display: flex;
    justify-content: space-between;
    align-items: baseline;
    font-size: 15px;
    white-space: nowrap;
  }
  .tagline { font-weight: 400; letter-spacing: 0.17em; color: var(--ink); text-transform: uppercase; }
  .website { font-weight: 700; letter-spacing: 0.09em; color: var(--ink); text-transform: uppercase; }
</style>
</head>
<body>
<main class="ad">
  <div class="band band--top"></div>

  <div class="word-row" style="top:30px"><span class="key key--wide">proven</span><span class="ghost">strategic practical</span></div>
  <div class="word-row" style="top:124px"><span class="ghost ghost--wide">collaborative cost effective</span></div>
  <div class="word-row" style="top:164px"><span class="ghost">trial ready proven</span><span class="key">strategic</span></div>
  <div class="word-row" style="top:260px"><span class="ghost">practical collaborative cost effective</span></div>
  <div class="word-row" style="top:327px"><span class="ghost ghost--wide">trialready proven strategic</span></div>
  <div class="word-row" style="top:370px"><span class="key">practical</span><span class="ghost ghost--mid">collaborative cost</span></div>
  <div class="word-row" style="top:463px"><span class="ghost">effective trial ready proven strategic</span></div>
  <div class="word-row" style="top:504px"><span class="ghost">practical</span><span class="key key--wide">collaborative</span></div>
  <div class="word-row" style="top:600px"><span class="ghost ghost--mid">cost effective trial readproven</span></div>
  <div class="word-row" style="top:667px"><span class="ghost ghost--mid">strategic practical collaborative</span></div>
  <div class="word-row" style="top:710px"><span class="key">costeffective</span><span class="ghost ghost--mid">trial ready</span></div>
  <div class="word-row" style="top:800px"><span class="ghost ghost--wide">proven strategic practical</span></div>
  <div class="word-row" style="top:870px"><span class="ghost ghost--wide">collaborative cost effective</span></div>
  <div class="word-row word-row--right" style="top:917px"><span class="key">trial ready</span></div>

  <div class="firm-name">
    <span class="firm-name__main">Thornbury</span>
    <span class="firm-name__sub">Legal Partners</span>
  </div>

  <svg class="cert-badge" width="120" height="46" viewBox="0 0 120 46" role="img" aria-label="Certification badge">
    <rect x="1" y="1" width="118" height="44" rx="7" fill="none" stroke="#231f20" stroke-width="1.5"/>
  </svg>

  <address class="contact" style="font-style:normal">
    415 555 0182<br>
    240 Harlan Street, Suite 900<br>
    San Francisco<br>
    CA 94108
  </address>

  <div class="footer-line">
    <span class="tagline">California Employment Law for Business</span>
    <span class="website">www.thornburylegalpartners.example</span>
  </div>

  <div class="band band--bottom"></div>
</main>
</body>
</html>
```